Business Card Design for a Handbags business

We are modernising our handbags website (see attached file for new front page) and are in need of a modern business card and a related design we can use on a small marquee at the markets, on letterhead, emails etc.

As the leather handbags we mostly import are from Italy, we want a smart modern European feel to the design. We are currently thinking about changing the name of the business from Meadowlark Handbags (see www.meadowlarkhandbags.com.au) to Vantera Handbags. Also open to other suggestions you may have that communicates the European influence and quality.

Target Market(s)

25-65 year old women (and some men)

Industry/Entity Type

Business

Contact Information for Business Card

Single or double sided - whichever creates more of an impact

Font styles to use
Serif
Sans Serif

Requirements
Must have
• Clean crisp look, slightly Italian or European look and feel to reflect where the handbags are imported from
Nice to have
• open to ideas

```html
<!DOCTYPE html>
<html lang="en">
<head>
<meta charset="utf-8">
<title>Vantera Handbags – Business Card</title>
<link rel="stylesheet" href="https://fonts.googleapis.com/css2?family=Crimson+Text&display=swap">
<style>
  :root {
    --leaf: #8dc63f;
    --leaf-soft: #e4f2d1;
    --ink: #231f20;
    --paper: #ffffff;
    --edge: #7a7a7a;
    --label: #222222;
  }
  * { box-sizing: border-box; margin: 0; padding: 0; }
  html, body {
    width: 1200px;
    height: 349px;
    overflow: hidden;
    background: var(--paper);
  }
  body {
    position: relative;
    font-family: "Crimson Text", "Palatino Linotype", Palatino, serif;
    color: var(--ink);
  }
  .side-label {
    position: absolute;
    top: 5px;
    font-size: 15px;
    color: var(--label);
  }
  .side-label--front { left: 22px; }
  .side-label--back { left: 614px; }

  .card {
    position: absolute;
    top: 28px;
    width: 571px;
    height: 301px;
    border: 1px solid var(--edge);
    background: var(--paper);
    overflow: hidden;
  }
  .card--front { left: 14px; }
  .card--back { left: 614px; }

  .card__band {
    position: absolute;
    left: 0;
    right: 0;
    bottom: 0;
    height: 43px;
    background: var(--leaf);
  }

  .flap-artwork {
    position: absolute;
    top: 0;
    left: 0;
    right: 0;
    height: 125px;
    background: linear-gradient(180deg, var(--leaf-soft) 0%, var(--paper) 100%);
  }

  .brand-name {
    position: absolute;
    left: 0;
    right: 0;
    text-align: center;
    font-weight: 400;
    line-height: 1;
    white-space: nowrap;
  }
  .brand-name--front {
    top: 200px;
    font-size: 51px;
  }
  .brand-name--back {
    top: 162px;
    font-size: 28px;
  }

  .contact {
    position: absolute;
    top: 198px;
    left: 0;
    right: 0;
    text-align: center;
    font-size: 16px;
    line-height: 18px;
    font-style: normal;
    white-space: nowrap;
  }
</style>
</head>
<body>
  <span class="side-label side-label--front">front</span>
  <span class="side-label side-label--back">back</span>

  <section class="card card--front">
    <div class="flap-artwork" role="img" aria-label="Illustration of a stitched handbag flap with a strap tab"></div>
    <h1 class="brand-name brand-name--front">Vantera Handbags</h1>
    <div class="card__band"></div>
  </section>

  <section class="card card--back">
    <h2 class="brand-name brand-name--back">Vantera Handbags</h2>
    <address class="contact">
      42 Corliss Street, HARTWELL ACT 2999<br>
      Telephone: 02 5550 1836, Claudia: 0400 555 274<br>
      Rita: 0400 555961, E-mail: info@meadowlarkhandbags.com.au
    </address>
    <div class="card__band"></div>
  </section>
</body>
</html>
```